Modern Lawfirm Business Card Design

We're looking for a business card to incorporate the newly created logo we had made.

Ideally looking for a law firm business card demonstrating, modern, minimalist, strong/bold design.

I'm open to any design honestly, but nothing "flashy".

Target Market(s)

Immigration law, family immigration, humanitarian, general legal

Industry/Entity Type

Law Firm

Contact Information for Business Card

Please use dummy information, name, street address, city, state, phone number, email, website.

Font styles to use
Serif
Sans Serif

Requirements
Must have
• Please use dummy information, name, street address, city, state, phone number, email, website.

```html
<!DOCTYPE html>
<html lang="en">
<head>
<meta charset="utf-8">
<title>Calderon Immigration Law – Business Card</title>
<link rel="stylesheet" href="https://fonts.googleapis.com/css2?family=EB+Garamond:wght@400;600&display=swap">
<style>
  :root {
    --navy: #1e4b8c;
    --navy-deep: #173f78;
    --navy-light: #2a5a9e;
    --paper: #ffffff;
    --paper-shade: #eeeeee;
    --ink: #1f1f1f;
    --ground: #f2f2f2;
  }
  * { margin: 0; padding: 0; box-sizing: border-box; }
  html, body {
    width: 1200px; height: 586px; overflow: hidden;
    background: var(--ground);
    font-family: "EB Garamond", Georgia, serif;
  }
  .canvas { position: relative; width: 1200px; height: 586px; }
  .card {
    position: absolute; top: 129px; width: 501px; height: 301px; overflow: hidden;
  }
  .card--front { left: 61px; }
  .card--back { left: 619px; }
  .card__texture { position: absolute; inset: 0; }
  .card--front .card__texture {
    background: linear-gradient(135deg, var(--navy-deep) 0%, var(--navy) 50%, var(--navy-light) 100%);
  }
  .card--back .card__texture {
    background: linear-gradient(135deg, var(--paper) 0%, var(--paper-shade) 55%, var(--paper) 100%);
  }

  /* Front */
  .front__website {
    position: absolute; left: 26px; top: 186px;
    color: var(--paper); font-size: 12px; font-weight: 600; letter-spacing: 3.6px;
  }
  .front__brand {
    position: absolute; left: 26px; top: 208px; width: 276px;
    color: var(--paper); font-weight: 400; text-align: center;
  }
  .front__brand-name { display: block; font-size: 42px; line-height: 46px; letter-spacing: 1px; }
  .front__brand-line { display: block; font-size: 10px; letter-spacing: 6px; margin-top: 4px; }

  /* Back */
  .back__brand {
    position: absolute; left: 0; right: 0; top: 36px;
    text-align: center; color: var(--navy); font-weight: 400;
  }
  .back__brand-name { display: block; font-size: 32px; line-height: 34px; letter-spacing: 1px; }
  .back__brand-line { display: block; font-size: 8px; letter-spacing: 5px; margin-top: 2px; }

  .back__person {
    position: absolute; right: 272px; top: 165px; text-align: right;
  }
  .back__name { color: var(--navy); font-size: 20px; font-weight: 600; line-height: 24px; }
  .back__role { color: var(--ink); font-size: 13px; line-height: 18px; }

  .back__divider {
    position: absolute; left: 249px; top: 127px; width: 2px; height: 112px;
    background: linear-gradient(to bottom, transparent, var(--navy) 30%, var(--navy) 70%, transparent);
  }

  .back__contacts {
    position: absolute; left: 280px; top: 143px; list-style: none;
  }
  .back__contact {
    display: flex; align-items: center; height: 29px;
    color: var(--ink); font-size: 14px;
  }
  .back__contact svg { width: 20px; height: 20px; margin-right: 8px; flex: none; }

  .back__address {
    position: absolute; left: 0; right: 0; top: 271px; text-align: center;
    color: var(--navy); font-size: 14px; font-weight: 600;
  }
</style>
</head>
<body>
<main class="canvas">

  <section class="card card--front" aria-label="Card front">
    <div class="card__texture" role="img" aria-label="Navy low-poly faceted background pattern"></div>
    <p class="front__website">www.calderonimmilaw.com</p>
    <p class="front__brand">
      <span class="front__brand-name">CALDERON</span>
      <span class="front__brand-line">IMMIGRATION LAW</span>
    </p>
  </section>

  <section class="card card--back" aria-label="Card back">
    <div class="card__texture" role="img" aria-label="White low-poly faceted background pattern"></div>
    <p class="back__brand">
      <span class="back__brand-name">CALDERON</span>
      <span class="back__brand-line">IMMIGRATION LAW</span>
    </p>

    <div class="back__person">
      <p class="back__name">Graham Ellery</p>
      <p class="back__role">Owner / Founder</p>
    </div>

    <div class="back__divider"></div>

    <ul class="back__contacts">
      <li class="back__contact">
        <svg viewBox="0 0 20 20" aria-hidden="true">
          <circle cx="10" cy="10" r="10" fill="var(--navy)"/>
          <path d="M5 8.5c0-1.5 2.2-2.5 5-2.5s5 1 5 2.5v.8h-2.3v-1h-5.4v1H5z" fill="#fff"/>
          <rect x="6.5" y="10" width="7" height="4" rx="1" fill="#fff"/>
        </svg>503-555-0142</li>
      <li class="back__contact">
        <svg viewBox="0 0 20 20" aria-hidden="true">
          <circle cx="10" cy="10" r="10" fill="var(--navy)"/>
          <rect x="7" y="5" width="6" height="3" fill="#fff"/>
          <rect x="5" y="8.5" width="10" height="4.5" rx="1" fill="#fff"/>
          <rect x="7" y="12" width="6" height="3" fill="#fff" stroke="var(--navy)" stroke-width=".6"/>
        </svg>1-877-555-0199</li>
      <li class="back__contact">
        <svg viewBox="0 0 20 20" aria-hidden="true">
          <circle cx="10" cy="10" r="10" fill="var(--navy)"/>
          <rect x="5" y="6.5" width="10" height="7" fill="#fff"/>
          <path d="M5 6.5l5 4 5-4" fill="none" stroke="var(--navy)" stroke-width="1"/>
        </svg>graham@calderonlaw.com</li>
    </ul>

    <p class="back__address">820 Alder Lane NW, Portland, OR 97210</p>
  </section>

</main>
</body>
</html>
```